Apartment services app

The app should permit current residents to pay rent, submit work orders or submit comments and general requests. There is an app that is available from Heron Works in the UK that could be used to benchmark, but I would like to see something more appropriate for the US.
Updates

The company name for this project is Oakfield Property Management. We will be providing a logo at a later date as we we will be submitting a separate design project for the development of a new logo.

Reason: I am extending the deadline by another week so that I may comment on the designs so far and each of you will have time to respond Tim

Target Market(s)

Residents of our apartment communities

Industry/Entity Type

Apartment

Requirements
Must have
• Ability to pay rent
• Ability to have reminders sent to resident
• Notices sent to resident
• Resident able to submit work order requests
• Resident able to submit comments and complaints

```html
<!DOCTYPE html>
<html lang="en">
<head>
<meta charset="utf-8">
<title>Oakfield Property Management – Repair Requests</title>
<link rel="stylesheet" href="https://fonts.googleapis.com/css2?family=Open+Sans:wght@400;600;700&display=swap">
<style>
  :root{
    --page-bg:#d9dadc;
    --status-bg:#333436;
    --header-bg:#4a4b4d;
    --header-text:#e6e6e6;
    --screen-bg:#e4e4e4;
    --card-bg:#ffffff;
    --title-text:#3c3c3c;
    --body-text:#9a9a9a;
    --accent:#e05555;
    --button-grey:#d3d3d3;
    --button-grey-text:#f4f4f4;
    --tab-bg:#3c3d3f;
    --tab-text:#b9b9b9;
    --tab-divider:#2e2f31;
    --divider:#d6d6d6;
  }
  *{box-sizing:border-box;margin:0;padding:0}
  html,body{width:1200px;height:900px;overflow:hidden}
  body{background:var(--page-bg);font-family:"Open Sans",Arial,sans-serif;display:flex;align-items:center;justify-content:center}
  .app-screen{width:484px;height:860px;background:var(--screen-bg);display:flex;flex-direction:column;overflow:hidden;box-shadow:0 10px 40px rgba(0,0,0,.18)}
  .status-bar{height:30px;flex:none;background:var(--status-bg);color:#fff;display:flex;align-items:center;justify-content:space-between;padding:0 12px;font-size:14px;font-weight:600}
  .carrier,.battery{display:flex;align-items:center;gap:6px;width:110px}
  .battery{justify-content:flex-end}
  .battery-icon{width:30px;height:13px;border:1.5px solid #fff;border-radius:2px;padding:1px}
  .battery-icon span{display:block;width:65%;height:100%;background:#fff}
  .app-header{height:62px;flex:none;background:var(--header-bg);color:var(--header-text);display:flex;align-items:center;justify-content:space-between;padding:0 16px}
  .app-header h1{font-size:17px;font-weight:400}
  .request-list{flex:1;padding:10px 12px;display:flex;flex-direction:column;gap:10px;min-height:0}
  .request-card{background:var(--card-bg);padding:20px 16px 16px;border-bottom:1px solid var(--divider);flex:1;display:flex;flex-direction:column;justify-content:space-between}
  .request-top{display:flex;gap:16px}
  .request-thumb{width:60px;height:60px;border-radius:50%;flex:none;margin-top:2px}
  .thumb-door{background:radial-gradient(circle at 45% 50%,#c9a55a,#e9dcc0 70%)}
  .thumb-wiring{background:radial-gradient(circle at 50% 50%,#8a8f96,#d8dadd 70%)}
  .thumb-leak{background:radial-gradient(circle at 50% 50%,#4a5566,#b7bcc4 70%)}
  .request-title{font-size:16px;font-weight:600;color:var(--title-text);margin-bottom:10px}
  .request-body p{font-size:12px;line-height:1.5;color:var(--body-text);margin-bottom:10px}
  .request-actions{display:flex;gap:8px}
  .btn{height:28px;font-family:inherit;font-size:12px;display:flex;align-items:center;justify-content:center;gap:6px;flex:1;border:0}
  .btn-send{background:var(--accent);color:#fff}
  .btn-muted{background:var(--button-grey);color:var(--button-grey-text)}
  .tab-bar{height:72px;flex:none;background:var(--tab-bg);display:flex}
  .tab{flex:1;display:flex;flex-direction:column;align-items:center;justify-content:center;gap:5px;color:var(--tab-text);font-size:11px;border-right:1px solid var(--tab-divider)}
  .tab:last-child{border-right:0}
</style>
</head>
<body>
<main class="app-screen">
  <div class="status-bar">
    <div class="carrier">
      <svg width="22" height="12" viewBox="0 0 22 12" fill="#fff"><rect x="0" y="8" width="3" height="4"/><rect x="5" y="6" width="3" height="6"/><rect x="10" y="4" width="3" height="8"/><rect x="15" y="2" width="3" height="10"/></svg>
      LUMEN
    </div>
    <div class="clock">10:35 AM</div>
    <div class="battery">65% <div class="battery-icon"><span></span></div></div>
  </div>

  <header class="app-header">
    <svg width="20" height="20" viewBox="0 0 24 24" fill="none" stroke="#cfcfcf" stroke-width="1.8"><circle cx="12" cy="12" r="3.2"/><path d="M12 2v3M12 19v3M2 12h3M19 12h3M4.9 4.9l2.1 2.1M17 17l2.1 2.1M4.9 19.1L7 17M17 7l2.1-2.1"/></svg>
    <h1>Repair Requests</h1>
    <svg width="20" height="20" viewBox="0 0 24 24" fill="none" stroke="#cfcfcf" stroke-width="1.8"><circle cx="12" cy="12" r="10"/><path d="M9.5 9a2.5 2.5 0 1 1 3.5 2.3c-.7.3-1 .9-1 1.7"/><circle cx="12" cy="17" r=".8" fill="#cfcfcf"/></svg>
  </header>

  <section class="request-list">
    <article class="request-card">
      <div class="request-top">
        <div class="request-thumb thumb-door" role="img" aria-label="Photo of a broken door handle"></div>
        <div class="request-body">
          <h2 class="request-title">Repair the broken door</h2>
          <p>Front door latch is loose and the frame is cracked near the lock.</p>
          <p>Please repair before the weekend. Access is fine during weekday mornings when someone is at home.</p>
        </div>
      </div>
      <div class="request-actions">
        <button class="btn btn-send"><svg width="11" height="11" viewBox="0 0 12 12" fill="#fff"><path d="M5 0h2v6h2.5L6 9.5 2.5 6H5z"/><rect y="10.5" width="12" height="1.5"/></svg>Send Request</button>
        <button class="btn btn-muted">Upload Photo</button>
        <button class="btn btn-muted"><svg width="11" height="11" viewBox="0 0 12 12" fill="#f4f4f4"><path d="M0 9.5V12h2.5L10 4.5 7.5 2z"/></svg>Edit</button>
      </div>
    </article>

    <article class="request-card">
      <div class="request-top">
        <div class="request-thumb thumb-wiring" role="img" aria-label="Photo of an electrician checking wiring"></div>
        <div class="request-body">
          <h2 class="request-title">Bad electricity wiring</h2>
          <p>Kitchen outlets spark when plugged in and the hallway light keeps flickering.</p>
          <p>Breaker trips twice a day. Would like an electrician to inspect the wiring soon.</p>
        </div>
      </div>
      <div class="request-actions">
        <button class="btn btn-send"><svg width="11" height="11" viewBox="0 0 12 12" fill="#fff"><path d="M5 0h2v6h2.5L6 9.5 2.5 6H5z"/><rect y="10.5" width="12" height="1.5"/></svg>Send Request</button>
        <button class="btn btn-muted">Upload Photo</button>
        <button class="btn btn-muted"><svg width="11" height="11" viewBox="0 0 12 12" fill="#f4f4f4"><path d="M0 9.5V12h2.5L10 4.5 7.5 2z"/></svg>Edit</button>
      </div>
    </article>

    <article class="request-card">
      <div class="request-top">
        <div class="request-thumb thumb-leak" role="img" aria-label="Photo of a plumber fixing a leaking pipe"></div>
        <div class="request-body">
          <h2 class="request-title">Water leaking</h2>
          <p>Water is leaking under the bathroom sink and pooling on the floor.</p>
          <p>Towels are down for now. A plumber visit this week would be appreciated.</p>
        </div>
      </div>
      <div class="request-actions">
        <button class="btn btn-send"><svg width="11" height="11" viewBox="0 0 12 12" fill="#fff"><path d="M5 0h2v6h2.5L6 9.5 2.5 6H5z"/><rect y="10.5" width="12" height="1.5"/></svg>Send Request</button>
        <button class="btn btn-muted">Upload Photo</button>
        <button class="btn btn-muted"><svg width="11" height="11" viewBox="0 0 12 12" fill="#f4f4f4"><path d="M0 9.5V12h2.5L10 4.5 7.5 2z"/></svg>Edit</button>
      </div>
    </article>
  </section>

  <nav class="tab-bar">
    <div class="tab">
      <svg width="24" height="24" viewBox="0 0 24 24" fill="none" stroke="#b9b9b9" stroke-width="1.6"><circle cx="12" cy="8" r="4"/><path d="M4 21c0-4.4 3.6-7 8-7s8 2.6 8 7z"/></svg>
      Account
    </div>
    <div class="tab">
      <svg width="24" height="24" viewBox="0 0 24 24" fill="none" stroke="#b9b9b9" stroke-width="1.6"><path d="M14.5 6.5a4 4 0 0 0 5 5L11 20a2.1 2.1 0 0 1-3-3l8.5-8.5a4 4 0 0 0-2-2z"/></svg>
      Services
    </div>
    <div class="tab">
      <svg width="24" height="24" viewBox="0 0 24 24" fill="none" stroke="#b9b9b9" stroke-width="1.6"><ellipse cx="12" cy="6" rx="7" ry="2.5"/><path d="M5 6v4c0 1.4 3.1 2.5 7 2.5s7-1.1 7-2.5V6M5 10v4c0 1.4 3.1 2.5 7 2.5s7-1.1 7-2.5v-4M5 14v4c0 1.4 3.1 2.5 7 2.5s7-1.1 7-2.5v-4"/></svg>
      Rents
    </div>
    <div class="tab">
      <svg width="24" height="24" viewBox="0 0 24 24" fill="none" stroke="#b9b9b9" stroke-width="1.6"><path d="M6 17V11a6 6 0 0 1 12 0v6l2 2H4z"/><path d="M10 21h4"/></svg>
      Notices
    </div>
  </nav>
</main>
</body>
</html>
```